Flyer Design Project- Wine Meditation

I require a flyer to be created for a course. It is a meditation course. So I want the cover design to look quirky but calm.

I have attached a previous design. The wording on the back should be the same only any reference to Chocolate should be changed to Wine. This project is for wine meditation. Although I have attached the previous flyer for guidance of the lay out and words used, I DO NOT want to to be a direct copy, I want it to look completely different. SO be creative. Any copies or anything that looks close to a copy will not even be considered.

I want the flyer to be A5 side but also the ability to resize it onto smaller cards.

I have also attached the wording for the back of the flyer in the attached word document.

If you need further information about the design breif please contact me.

Target Market(s)

20 to 40

Requirements
Must have
• Must have space for a logo which is currently being designed by the pixel harbour. For the time being insert the tall maple glen wellness logo which is attached.

Picture something realted to wine on the front and course detail on the back same as the attached sample.
Should not have
• a direct copy of my samples I have attached.

```html
<!DOCTYPE html>
<html lang="en">
<head>
<meta charset="utf-8">
<title>Wine Meditation Course</title>
<link rel="stylesheet" href="https://fonts.googleapis.com/css2?family=Archivo+Black&family=Arimo:wght@400;700&display=swap">
<style>
  :root {
    --maroon: #5e1537;
    --maroon-deep: #4f1030;
    --accent-red: #e8472a;
    --white: #ffffff;
    --veil: rgba(255, 255, 255, 0.86);
    --veil-soft: rgba(255, 255, 255, 0.8);
    --cream: #f3e6a8;
  }
  * { margin: 0; padding: 0; box-sizing: border-box; }
  html, body { width: 846px; height: 1200px; overflow: hidden; background: #fff; }
  .flyer {
    position: relative;
    width: 846px;
    height: 1200px;
    overflow: hidden;
    font-family: "Arimo", Arial, sans-serif;
    color: var(--maroon);
  }
  .backdrop {
    position: absolute; inset: 0;
    background:
      radial-gradient(ellipse 260px 380px at 130px 330px, rgba(120, 20, 30, 0.75), transparent 75%),
      radial-gradient(ellipse 300px 420px at 580px 180px, rgba(255, 235, 230, 0.5), transparent 70%),
      linear-gradient(180deg, #b9767e 0%, #c48a88 18%, #d6a598 36%, #d9ab8e 52%, #d9b278 66%, #c9b15a 80%, #a9a23a 100%);
  }
  .backdrop::after {
    content: ""; position: absolute; inset: 0;
    background: linear-gradient(90deg, rgba(90, 20, 50, 0.15) 0%, transparent 40%, rgba(90, 20, 60, 0.35) 100%);
  }
  .grapes {
    position: absolute; left: 280px; top: 960px; width: 566px; height: 240px;
    background: radial-gradient(ellipse at 40% 50%, #c8d46a 0%, #a8b94a 45%, rgba(140, 160, 50, 0) 80%);
  }
  .title {
    position: absolute; left: 56px; top: 52px;
    font-family: "Arimo", Arial, sans-serif; font-weight: 700;
    font-size: 64px; line-height: 72px; color: var(--white);
    letter-spacing: -0.5px;
  }
  .band {
    position: absolute; background: var(--white);
    font-family: "Archivo Black", "Arial Black", sans-serif;
    color: var(--maroon); text-transform: uppercase;
  }
  .band--wine-what { left: 451px; top: 157px; width: 395px; height: 44px; padding: 10px 0 0 5px; font-size: 21px; }
  .band--hangover {
    left: 0; top: 416px; width: 451px; height: 84px;
    padding: 11px 0 0 0; text-align: right; font-size: 23px; line-height: 31px;
  }
  .band--what-you-get { left: 451px; top: 718px; width: 395px; height: 47px; padding: 10px 0 0 2px; font-size: 23px; }
  .panel { position: absolute; font-size: 16.5px; line-height: 23.8px; color: var(--maroon); }
  .panel--intro { left: 451px; top: 221px; width: 395px; height: 168px; background: var(--veil); padding: 31px 10px 0 0; }
  .panel--hangover { left: 0; top: 523px; width: 451px; height: 195px; background: var(--veil-soft); padding: 28px 12px 0 72px; }
  .panel--list { left: 451px; top: 784px; width: 395px; height: 196px; background: var(--veil); padding: 16px 0 0 0; font-size: 16.5px; line-height: 24.2px; }
  .highlight { color: var(--accent-red); }
  .course-list { list-style: none; }
  .course-list li:nth-child(odd) { color: var(--accent-red); }
  .course-list li:nth-child(even) { color: var(--maroon); }
  .photo {
    position: absolute; left: 451px; top: 416px; width: 395px; height: 302px;
    background:
      radial-gradient(ellipse 120px 150px at 60% 45%, #e6bba6 0%, rgba(200, 150, 130, 0) 80%),
      linear-gradient(90deg, #6b5a4a 0%, #9c8a72 40%, #d4c2a8 70%, #8a7a60 100%);
  }
  .brand-mark {
    position: absolute; left: 24px; top: 965px; width: 80px; height: 161px;
    display: flex; flex-direction: column; align-items: center; gap: 10px;
  }
  .brand-mark__square { width: 60px; height: 60px; background: var(--white); }
  .brand-mark__name {
    font-weight: 700; font-size: 14px; line-height: 17px;
    color: var(--white); text-align: center; text-transform: uppercase;
  }
  .credit {
    position: absolute; left: 114px; top: 1058px;
    font-weight: 700; font-size: 15px; line-height: 26px; color: var(--white);
  }
  .credit__caps { text-transform: uppercase; font-size: 13.5px; }
  .credit__name { color: var(--cream); font-weight: 400; }
  .credit__name strong { font-weight: 700; }
  .phone { position: absolute; left: 26px; top: 1146px; font-weight: 700; font-size: 20px; color: var(--white); }
  .web-bar {
    position: absolute; left: 451px; top: 1126px; width: 395px; height: 74px;
    background: var(--maroon-deep); color: var(--white);
    font-weight: 700; font-size: 18px; padding: 22px 0 0 5px;
  }
</style>
</head>
<body>
<div class="flyer">
  <div class="backdrop" role="img" aria-label="Soft-focus photograph of glasses of red and white wine"></div>
  <div class="grapes" role="img" aria-label="Photograph of green grapes and vine leaves"></div>

  <h1 class="title">Wine<br>Meditation<br>Course</h1>

  <h2 class="band band--wine-what">Wine what?!</h2>
  <p class="panel panel--intro">Yes you read right. <span class="highlight">Wine meditation!</span><br>What could be better than combining the dilatable taste of wine with meditation, right? Well that is exactly what this course is all about with a little bit of Mindfulness<br>thrown in.</p>

  <h2 class="band band--hangover">Learn to drink wine<br>without the hangover!</h2>
  <p class="panel panel--hangover">&nbsp;NO HANGOVER! Really? It's true because we challenge you to the fact that you have never really savoured your glass of wine. So we are going to teach you how to do it mindfully. This way you are guaranteed not to get a hangover while drinking wine.</p>

  <div class="photo" role="img" aria-label="Photograph of a woman holding a glass of red wine"></div>

  <h2 class="band band--what-you-get">What you get:</h2>
  <div class="panel panel--list">
    <ul class="course-list">
      <li>A Wine Meditation course book</li>
      <li>Mindfulness and meditation instruction online</li>
      <li>Learn how to drink wine mindfully</li>
      <li>Learn Meditation techniques and postures</li>
      <li>FREE mp3 Guided Meditation download</li>
      <li>5% of the course goes to charity — Please see our website for this mont's charitable cause</li>
    </ul>
  </div>

  <div class="brand-mark">
    <div class="brand-mark__square"></div>
    <div class="brand-mark__name">Tall Maple Glen Wellness</div>
  </div>
  <p class="credit">
    <span class="credit__caps">Brought to you</span><br>
    by <span class="credit__name">TALL MAPLE GLEN</span><br>
    <span class="credit__name"><strong>Wellness</strong></span>
  </p>
  <p class="phone">Phone (02) 5550 1847</p>

  <div class="web-bar">www.Maple-meditation.com.au</div>
</div>
</body>
</html>
```